Online Art Gallery & Art Management Firm looking for a business card

I'm launching an online art gallery (paintings, photography, drawings, furniture, books, ...) where people can buy all types of art. It's a platform where young and unknown artists can showcase their oeuvre.

Additionally, the venture will act as my advising company for artists. I help them out with their business side of life and become their representative.

The company name: The Velvet Parlour
Logo is attached

I'm looking for something very classy and upmarket.
Updates

Reason: Logo wasn't finished yet...

The design should include the following information: - Name: Pieter Vandomme - Title: Founder - Mobile: +32 (0) 486 514 362 - E-mail: pieter@velvet-parlour.example - Website www.velvet-parlour.example I prefer the have the logo (without website) on the one side and the information on the other. Best regards Pieter

Target Market(s)

Art buyers / art dealers / artists / middle class / upmarket /

Industry/Entity Type

Artists

Colors

Designer to choose colors to be used in the design.

Requirements
Must have
• Must communicate credibility, trust and integrity
Nice to have
• Something classy, chique
Should not have
• Nothing to artistic or creative

```html
<!DOCTYPE html>
<html lang="en">
<head>
<meta charset="utf-8">
<title>The Velvet Parlour — Business Card</title>
<link rel="stylesheet" href="https://fonts.googleapis.com/css2?family=Cormorant+Garamond:wght@400;500;700&display=swap">
<style>
  :root {
    --backdrop: #2c2928;
    --card-dark: #16181c;
    --card-light: #f0f0f0;
    --ink-dark: #2a2b2e;
    --ink-silver: #a4a6aa;
    --ink-silver-soft: #8d9094;
    --serif: "Cormorant Garamond", Georgia, serif;
  }
  * { box-sizing: border-box; margin: 0; padding: 0; }
  html, body {
    width: 1200px;
    height: 1000px;
    overflow: hidden;
    background: var(--backdrop);
    font-family: var(--serif);
  }
  .canvas {
    position: relative;
    width: 1200px;
    height: 1000px;
  }
  .card {
    position: absolute;
    left: 215px;
    width: 770px;
    height: 440px;
    overflow: hidden;
    box-shadow: 0 18px 40px rgba(0, 0, 0, 0.45);
  }
  .card--front { top: 40px; background: var(--card-light); }
  .card--back { top: 520px; background: var(--card-dark); }
  .card__shape {
    position: absolute;
    inset: 0;
    width: 100%;
    height: 100%;
  }
  .wordmark {
    position: absolute;
    font-family: var(--serif);
    font-weight: 400;
    text-transform: uppercase;
    white-space: nowrap;
  }
  .card--front .wordmark {
    left: 70px;
    top: 232px;
    font-size: 44px;
    letter-spacing: 10px;
    color: var(--ink-dark);
  }
  .card--back .wordmark {
    left: 60px;
    top: 150px;
    font-size: 30px;
    letter-spacing: 7px;
    color: var(--ink-silver);
  }
  .holder {
    position: absolute;
    left: 60px;
    top: 240px;
  }
  .holder__name {
    font-size: 30px;
    font-weight: 500;
    letter-spacing: 1px;
    color: var(--ink-silver);
  }
  .holder__title {
    margin-top: 2px;
    font-size: 15px;
    font-weight: 700;
    letter-spacing: 2px;
    text-transform: uppercase;
    color: var(--ink-silver);
  }
  .contacts {
    position: absolute;
    left: 60px;
    top: 318px;
    list-style: none;
  }
  .contacts__item {
    display: flex;
    align-items: center;
    height: 34px;
    font-size: 18px;
    color: var(--ink-silver-soft);
  }
  .contacts__icon {
    width: 22px;
    height: 22px;
    margin-right: 18px;
    flex: none;
  }
</style>
</head>
<body>
<main class="canvas">

  <section class="card card--front" aria-label="Business card, logo side">
    <svg class="card__shape" viewBox="0 0 770 440" aria-hidden="true">
      <polygon points="420,0 770,0 770,100 600,175" fill="var(--card-dark)"/>
    </svg>
    <p class="wordmark">The Velvet Parlour</p>
  </section>

  <section class="card card--back" aria-label="Business card, contact side">
    <svg class="card__shape" viewBox="0 0 770 440" aria-hidden="true">
      <polygon points="430,0 770,0 770,215 625,140" fill="var(--card-light)"/>
    </svg>
    <p class="wordmark">The Velvet Parlour</p>

    <div class="holder">
      <p class="holder__name">Pieter Vandomme</p>
      <p class="holder__title">Founder</p>
    </div>

    <ul class="contacts">
      <li class="contacts__item">
        <svg class="contacts__icon" viewBox="0 0 24 24" aria-hidden="true">
          <path d="M3 8c3-3 15-3 18 0v3h-5V9H8v2H3z" fill="var(--ink-silver-soft)"/>
          <path d="M6 13h12l2 8H4z" fill="var(--ink-silver-soft)"/>
          <circle cx="12" cy="17" r="2" fill="var(--card-dark)"/>
        </svg>
        <span>+32 (0) 486 514 362</span>
      </li>
      <li class="contacts__item">
        <svg class="contacts__icon" viewBox="0 0 24 24" aria-hidden="true">
          <rect x="2" y="5" width="20" height="14" fill="var(--ink-silver-soft)"/>
          <path d="M2 5l10 8 10-8M2 19l7-7M22 19l-7-7" stroke="var(--card-dark)" stroke-width="1.5" fill="none"/>
        </svg>
        <span>pieter@velvet-parlour.example</span>
      </li>
      <li class="contacts__item">
        <svg class="contacts__icon" viewBox="0 0 24 24" aria-hidden="true">
          <rect x="2.5" y="3.5" width="19" height="13" rx="1" stroke="var(--ink-silver-soft)" stroke-width="2" fill="none"/>
          <path d="M9 21h6M12 17v4" stroke="var(--ink-silver-soft)" stroke-width="2"/>
        </svg>
        <span>www.velvet-parlour.example</span>
      </li>
    </ul>
  </section>

</main>
</body>
</html>
```